New Business Card Design Project

Details for my new Business Card Design Project will be added soon. Like a nice simple design

Target Market(s)

Home improvement

Industry/Entity Type

Home Improvement

Contact Information for Business Card

Roofing siding gutters additions garages decks

Requirements
Must have
• Phone 5097362418
• Email korvandpm@mailnest.net

```html
<!DOCTYPE html>
<html lang="en">
<head>
<meta charset="utf-8">
<title>Korvand Contracting – Business Cards</title>
<link rel="stylesheet" href="https://fonts.googleapis.com/css2?family=Open+Sans:wght@400;600;700&display=swap">
<style>
  :root {
    --blue-light: #1878bd;
    --blue: #115fa3;
    --blue-deep: #0c4c8a;
    --paper: #f4f4f4;
    --paper-shade: #e4e4e4;
    --white: #ffffff;
    --backdrop: #d9d6d0;
  }
  * { margin: 0; padding: 0; box-sizing: border-box; }
  html, body {
    width: 1200px; height: 1023px; overflow: hidden;
    background: var(--backdrop);
    font-family: "Open Sans", sans-serif;
  }
  .canvas {
    position: relative; width: 1200px; height: 1023px;
  }
  .card {
    position: absolute; left: 250px; width: 700px; height: 400px;
    border-radius: 22px; overflow: hidden;
    box-shadow: 0 12px 30px rgba(0,0,0,.25);
  }
  /* Front */
  .card-front {
    top: 60px;
    background: radial-gradient(circle at 50% 35%, var(--blue-light) 0%, var(--blue) 55%, var(--blue-deep) 100%);
    color: var(--white);
  }
  .brand {
    display: flex; align-items: center; gap: 16px;
  }
  .brand-square { width: 26px; height: 26px; }
  .brand-name { font-weight: 600; letter-spacing: .5px; }
  .card-front .brand {
    position: absolute; left: 0; right: 0; top: 160px; justify-content: center;
  }
  .card-front .brand-square { background: var(--white); }
  .card-front .brand-name { font-size: 40px; color: var(--white); }
  .front-phone {
    position: absolute; right: 150px; top: 245px;
    display: flex; align-items: center; gap: 8px;
    font-size: 19px; letter-spacing: 2px;
  }
  /* Back */
  .card-back { top: 560px; background: var(--paper); display: flex; }
  .info-band {
    width: 290px; height: 100%;
    background: linear-gradient(180deg, var(--blue) 0%, var(--blue-deep) 100%);
    color: var(--white); padding: 34px 26px 26px 34px; position: relative;
  }
  .person-name { font-size: 26px; font-weight: 700; margin-bottom: 14px; }
  .contact-line {
    display: flex; align-items: center; gap: 10px;
    font-size: 15px; margin-bottom: 8px; letter-spacing: .5px;
  }
  .services {
    position: absolute; right: 22px; bottom: 22px; text-align: right;
    list-style: none; font-size: 15px; line-height: 1.45;
  }
  .services-title { font-weight: 700; }
  .services li::after { content: " •"; }
  .services .services-title::after { content: ""; }
  .brand-panel {
    flex: 1;
    background: linear-gradient(160deg, var(--white) 0%, var(--paper) 60%, var(--paper-shade) 100%);
    display: flex; align-items: center; justify-content: center;
  }
  .brand-panel .brand-square { background: var(--blue); }
  .brand-panel .brand-name { font-size: 32px; color: var(--blue); }
  .icon { width: 16px; height: 16px; flex: none; }
</style>
</head>
<body>
<main class="canvas">
  <section class="card card-front">
    <div class="brand">
      <span class="brand-square"></span>
      <span class="brand-name">Korvand Contracting</span>
    </div>
    <div class="front-phone">
      <svg class="icon" viewBox="0 0 16 16"><circle cx="8" cy="8" r="7" fill="none" stroke="#fff" stroke-width="1.4"/><path d="M5.5 4.5l1.5 0 .6 2-1 .8a5 5 0 0 0 2.1 2.1l.8-1 2 .6v1.5c-3.5.3-6.3-2.5-6-6z" fill="#fff"/></svg>
      <span>5097362418</span>
    </div>
  </section>

  <section class="card card-back">
    <div class="info-band">
      <h1 class="person-name">Dorian Korvand</h1>
      <p class="contact-line">
        <svg class="icon" viewBox="0 0 16 16"><circle cx="8" cy="8" r="7" fill="none" stroke="#fff" stroke-width="1.4"/><path d="M5.5 4.5l1.5 0 .6 2-1 .8a5 5 0 0 0 2.1 2.1l.8-1 2 .6v1.5c-3.5.3-6.3-2.5-6-6z" fill="#fff"/></svg>
        <span>5097362418</span>
      </p>
      <p class="contact-line">
        <svg class="icon" viewBox="0 0 16 16"><rect x="1.5" y="3.5" width="13" height="9" fill="none" stroke="#fff" stroke-width="1.3"/><path d="M1.5 3.5l6.5 5 6.5-5" fill="none" stroke="#fff" stroke-width="1.3"/></svg>
        <span>korvandpm@mailnest.net</span>
      </p>
      <ul class="services">
        <li class="services-title">We Offer</li>
        <li>Roofing</li>
        <li>Siding</li>
        <li>Gutter</li>
        <li>Additions</li>
        <li>Decks</li>
        <li>Handyman Services</li>
      </ul>
    </div>
    <div class="brand-panel">
      <div class="brand">
        <span class="brand-square"></span>
        <span class="brand-name">Korvand Contracting</span>
      </div>
    </div>
  </section>
</main>
</body>
</html>
```